Ferncastle Financial - Website Design

We need a website design for a new commercial real estate company called Ferncastle Financial. We're effectively commercial mortgage brokers connecting real estate investors to lenders. We need a website that is simple (not busy), elegant, professional, and user-friendly. A lot of the users will be in their 50's and less tech savvy, so a stream-lined design is best. The website will serve as a portal for lenders to review new financing opportunities, as well as for real estate investors to review terms from lenders.
Updates
Just uploaded our logo.
Target Market(s)
Commercial real estate investors and lenders
Industry/Entity Type
Real Estate
Number of Pages Required
1 page
Colors
Designer to choose colors to be used in the design.
Look and feel

```html
<!DOCTYPE html>
<html lang="en">
<head>
<meta charset="utf-8">
<title>Ferncastle Financial</title>
<link rel="stylesheet" href="https://fonts.googleapis.com/css2?family=Mulish:wght@400;600;700;800&display=swap">
<style>
:root{
  --navy:#172a45;
  --navy-soft:#1f3658;
  --ink:#2b2f36;
  --muted:#555b63;
  --light:#f2f3f5;
  --line:#d9dde2;
  --footer:#353535;
  --white:#ffffff;
}
*{margin:0;padding:0;box-sizing:border-box}
html,body{width:760px;height:1200px;overflow:hidden;background:var(--white)}
body{font-family:"Mulish",Arial,sans-serif;color:var(--ink);position:relative}
.abs{position:absolute}

/* header */
.site-header{left:0;top:0;width:760px;height:60px;background:var(--white);box-shadow:0 1px 3px rgba(0,0,0,.12);z-index:2}
.brand{left:102px;top:16px;display:flex;align-items:center;gap:7px}
.brand-dot{width:24px;height:24px;border-radius:50%;background:var(--navy)}
.brand-name{font-weight:700;font-size:12px;color:var(--navy);letter-spacing:.4px}
.contact{top:9px;right:131px;display:flex;gap:22px;font-size:8.5px;color:var(--navy);align-items:center}
.contact span{display:flex;align-items:center;gap:5px}
.main-nav{top:34px;right:131px;display:flex;gap:21px;font-size:7px;letter-spacing:.3px;color:var(--navy)}
.main-nav a{color:inherit;text-decoration:none;padding-bottom:5px}
.main-nav a.active{border-bottom:2px solid var(--navy);padding:0 8px 5px}

/* hero */
.hero{left:0;top:60px;width:760px;height:227px;background:linear-gradient(100deg,#c9d6d8 0%,#dfe6e7 45%,#eef1f1 70%,#d7dcdc 100%)}
.hero-title{left:103px;top:127px;font-size:30px;line-height:38px;font-weight:400;color:var(--navy);z-index:1}

/* welcome */
.welcome{left:0;top:287px;width:760px;height:118px;background:var(--navy);color:var(--white);padding:22px 103px 0}
.welcome h2{font-size:15px;font-weight:400;margin-bottom:8px}
.welcome p{font-size:8.4px;line-height:14px}

/* services */
.service{width:130px;text-align:center;top:436px}
.service-icon{width:80px;height:80px;border-radius:50%;background:var(--navy);margin:0 auto;display:flex;align-items:center;justify-content:center}
.service h3{font-size:12.3px;font-weight:800;color:var(--navy);margin-top:20px;letter-spacing:.2px}
.service p{font-size:7.3px;line-height:10.5px;color:var(--muted);margin-top:6px}

/* help */
.help{left:0;top:631px;width:760px;height:280px;background:var(--light)}
.help-card{width:150px;text-align:center;top:659px}
.help-card h4{font-size:8.3px;font-weight:400;line-height:11px;color:var(--ink);height:26px}
.help-photo{width:92px;height:92px;border-radius:50%;margin:9px auto 0;border:1.5px solid var(--navy);position:relative}
.help-badge{position:absolute;left:-20px;top:-3px;width:38px;height:38px;border-radius:50%;background:var(--white);border:1.5px solid var(--navy)}
.help-card p{font-size:7.3px;line-height:10.5px;color:var(--ink);margin-top:13px;height:30px}
.help-card a{display:inline-block;margin-top:9px;font-size:9.5px;font-weight:800;color:var(--navy);text-decoration:none}

/* reverse mortgage */
.reverse-title{left:103px;top:937px;font-size:11.8px;font-weight:600;color:var(--ink)}
.reverse-list{left:103px;top:961px;list-style:none;font-size:9px;color:var(--muted)}
.reverse-list li{display:flex;align-items:center;gap:8px;height:17px}
.reverse-image{left:374px;top:961px;width:283px;height:159px;background:radial-gradient(ellipse at 60% 60%,#e6e2dc 0%,#ede8e2 40%,#f7f7f7 75%,#ffffff 100%)}

/* footer */
.site-footer{left:0;top:1120px;width:760px;height:80px;background:var(--footer);color:var(--white)}
.footer-brand{left:103px;top:1147px;display:flex;align-items:center;gap:7px}
.footer-brand .brand-dot{background:var(--white)}
.footer-brand .brand-name{color:var(--white)}
.footer-nav{right:138px;top:1150px;font-size:6.7px;display:flex;gap:8px}
.footer-nav a{color:var(--white);text-decoration:none}
.copyright{right:139px;top:1167px;font-size:6.3px}
</style>
</head>
<body>

<header class="site-header abs">
  <div class="brand abs"><span class="brand-dot"></span><span class="brand-name">FERNCASTLE FINANCIAL</span></div>
  <div class="contact abs">
    <span><svg width="9" height="10" viewBox="0 0 10 10"><path d="M2 0 L4 2.5 L3 4 Q4.5 6.5 6 7 L7.5 6 L10 8 L8.5 10 Q2 9 0 1.5 Z" fill="#172a45"/></svg>(123) 123-456</span>
    <span><svg width="11" height="8" viewBox="0 0 11 8"><rect x=".5" y=".5" width="10" height="7" fill="none" stroke="#172a45"/><path d="M.5 .5 L5.5 4.5 L10.5 .5" fill="none" stroke="#172a45"/></svg>office@example.com</span>
  </div>
  <nav class="main-nav abs">
    <a class="active" href="#">HOME</a><a href="#">LENDERS</a><a href="#">INVESTORS</a><a href="#">CONTACT US</a>
  </nav>
</header>

<section class="hero abs" role="img" aria-label="Hands signing mortgage papers behind a small model house"></section>
<h1 class="hero-title abs">Got a Mortgage<br>that you need to protect?</h1>

<section class="welcome abs">
  <h2>Welcome to Our Company!</h2>
  <p>Lorem ipsum dolor sit amet, consectetuer adipiscing elit. Aenean commodo ligula eget dolor. Aenean massa. Cum sociis natoque penatibus et magnis dis parturient montes, nascetur ridiculus mus. Donec quam felis, ultricies nec, pellentesque eu, pretium quis, sem. Nulla consequat massa quis enim. Donec pede justo, fringilla vel, aliquet nec, vulputate eget, arcu.</p>
</section>

<div class="service abs" style="left:108px">
  <div class="service-icon"><svg width="26" height="38" viewBox="0 0 26 38" fill="none" stroke="#fff" stroke-width="2.5"><rect x="2" y="2" width="22" height="34"/><path d="M13 2V24M2 13H24M2 24H24"/><path d="M10 36V28H16V36" fill="#fff"/></svg></div>
  <h3>APARTMENTS</h3>
  <p>Aliquam dictum elit vitae mauris facilisis, at dictum urna dignissim donec vel lectus vel felis.</p>
</div>
<div class="service abs" style="left:243px">
  <div class="service-icon"><svg width="40" height="38" viewBox="0 0 40 38" fill="none" stroke="#fff" stroke-width="2.5"><path d="M2 18 L20 3 L38 18"/><path d="M7 15V36H33V15"/><rect x="11" y="20" width="7" height="7"/><rect x="22" y="22" width="7" height="14" fill="#fff"/><path d="M29 4V10"/></svg></div>
  <h3>HOUSES</h3>
  <p>Aliquam dictum elit vitae mauris facilisis, at dictum urna dignissim donec vel lectus vel felis.</p>
</div>
<div class="service abs" style="left:384px">
  <div class="service-icon"><svg width="42" height="30" viewBox="0 0 42 30" fill="none" stroke="#fff" stroke-width="2.5"><path d="M8 12 L12 3 H30 L34 12"/><rect x="3" y="12" width="36" height="11" rx="3"/><circle cx="10" cy="17.5" r="2"/><circle cx="32" cy="17.5" r="2"/><path d="M16 18H26"/><path d="M7 23V28H12V23M30 23V28H35V23"/></svg></div>
  <h3>GARAGES</h3>
  <p>Aliquam dictum elit vitae mauris facilisis, at dictum urna dignissim donec vel lectus vel felis.</p>
</div>
<div class="service abs" style="left:528px">
  <div class="service-icon"><svg width="38" height="38" viewBox="0 0 38 38" fill="none" stroke="#fff" stroke-width="2.5"><path d="M4 2H34L36 11H2Z"/><path d="M2 11Q5 15 9.5 11Q14 15 19 11Q24 15 28.5 11Q33 15 36 11"/><path d="M4 13V36H34V13"/><path d="M11 29L19 23L27 29Z"/><path d="M19 23V20"/></svg></div>
  <h3>COMMERCIAL</h3>
  <p>Aliquam dictum elit vitae mauris facilisis, at dictum urna dignissim donec vel lectus vel felis.</p>
</div>

<section class="help abs"></section>
<div class="help-card abs" style="left:125px">
  <h4>Get A Mortgage THAT<br>YOU NEED TO PROTECT?</h4>
  <div class="help-photo" role="img" aria-label="Worried couple reviewing their mortgage" style="background:linear-gradient(135deg,#e9e4df,#b9a596 55%,#f1eeea)"><span class="help-badge"></span></div>
  <p>Personalized to your situation. Compare lenders, payments and interest.</p>
  <a href="#">Get You Protect Now &rsaquo;</a>
</div>
<div class="help-card abs" style="left:299px">
  <h4>Reduce interest to<br>RESOLVE DEBT</h4>
  <div class="help-photo" role="img" aria-label="Man raising his arms at sunrise over a field" style="background:linear-gradient(180deg,#d9c98a 0%,#a7a15e 45%,#4f6b2c 100%)"><span class="help-badge"></span></div>
  <p>Consolidate your debt with our quality Debt Relief Solutions.</p>
  <a href="#">Get Help &rsaquo;</a>
</div>
<div class="help-card abs" style="left:478px">
  <h4>Do you have any<br>QUESTIONS?</h4>
  <div class="help-photo" role="img" aria-label="Family talking with a financial adviser" style="background:linear-gradient(135deg,#e4e8ec,#b3b9c0 50%,#eef0f2)"><span class="help-badge"></span></div>
  <p>Start a 1-on-1 discussion with our financial experts.</p>
  <a href="#">Ask a Question &rsaquo;</a>
</div>

<h3 class="reverse-title abs">Reverse mortgages are a smart retirement option for those who qualify:</h3>
<ul class="reverse-list abs">
  <li><svg width="10" height="10" viewBox="0 0 10 10" fill="none" stroke="#172a45" stroke-width="1.4"><path d="M2 3A4 4 0 1 1 2 7"/><path d="M1 1V3.5H3.5"/><path d="M5 3V5.5L6.5 6.5"/></svg>Homeowner must be 62 or older</li>
  <li><svg width="10" height="10" viewBox="0 0 10 10" fill="none" stroke="#172a45" stroke-width="1.4"><path d="M2 3A4 4 0 1 1 2 7"/><path d="M1 1V3.5H3.5"/><path d="M5 3V5.5L6.5 6.5"/></svg>Your house is your primary residence</li>
  <li><svg width="10" height="10" viewBox="0 0 10 10" fill="none" stroke="#172a45" stroke-width="1.4"><path d="M2 3A4 4 0 1 1 2 7"/><path d="M1 1V3.5H3.5"/><path d="M5 3V5.5L6.5 6.5"/></svg>Not delinquent on any federal debt</li>
  <li><svg width="10" height="10" viewBox="0 0 10 10" fill="none" stroke="#172a45" stroke-width="1.4"><path d="M2 3A4 4 0 1 1 2 7"/><path d="M1 1V3.5H3.5"/><path d="M5 3V5.5L6.5 6.5"/></svg>You must discuss the program with a counsellor</li>
</ul>
<div class="reverse-image abs" role="img" aria-label="Couple embracing in front of a sketched family house"></div>

<footer class="site-footer abs"></footer>
<div class="footer-brand abs"><span class="brand-dot"></span><span class="brand-name">FERNCASTLE FINANCIAL</span></div>
<nav class="footer-nav abs"><a href="#">HOME</a>|<a href="#">LENDERS</a>|<a href="#">INVESTORS</a>|<a href="#">CONTACT US</a></nav>
<p class="copyright abs">&copy; Ferncastle Financial. All rights reserved.</p>

</body>
</html>
```